Business Card Design Project

I would like a business card created for a new company. This is a holding company that acts as my investment company. It holds real estate and service based companies. The name of the company is Lucernaria which is Italian for Lanternry. Defined as development or growth.
We currently have no logo. I really like some of the "different" cards out there. Potentially metallic or grey/black. That looks premium/hi-end and unique. I am not sure if your design would be specific to the card stock I end with our just logo/design/font.
Real Estate

```html
<!DOCTYPE html>
<html lang="en">
<head>
<meta charset="utf-8">
<title>Lucernaria — Business Card</title>
<link rel="stylesheet" href="https://fonts.googleapis.com/css2?family=Bebas+Neue&display=swap">
<style>
  :root {
    --page-bg-top: #f4f4f8;
    --page-bg-bottom: #dcdce4;
    --metal-light: #c9c9c9;
    --metal-mid: #8f8f8f;
    --metal-dark: #5e5e5e;
    --ink: #2b2b2b;
    --edge: #e6e6e6;
  }
  * { box-sizing: border-box; margin: 0; padding: 0; }
  html, body { width: 1200px; height: 900px; overflow: hidden; }
  body {
    background: radial-gradient(ellipse at 50% 45%, var(--page-bg-top) 0%, var(--page-bg-bottom) 100%);
    font-family: "Bebas Neue", "Oswald", sans-serif;
    color: var(--ink);
  }
  .canvas {
    width: 1200px; height: 900px;
    display: flex; align-items: center; justify-content: center; gap: 60px;
  }
  .card {
    position: relative;
    width: 490px; height: 280px;
    border: 1px solid var(--edge);
    background:
      repeating-linear-gradient(0deg, rgba(255,255,255,0.07) 0 1px, rgba(0,0,0,0.06) 1px 2px, rgba(255,255,255,0) 2px 3px),
      linear-gradient(115deg, var(--metal-dark) 0%, var(--metal-mid) 22%, var(--metal-light) 38%, var(--metal-mid) 55%, var(--metal-dark) 72%, var(--metal-mid) 88%, var(--metal-light) 100%);
    overflow: hidden;
  }
  .card--front { display: flex; align-items: center; justify-content: center; }
  .brand-name {
    font-size: 92px;
    font-weight: 400;
    letter-spacing: 1px;
    line-height: 1;
    color: var(--ink);
  }
  .card--back { padding: 26px 34px; }
  .holder-name { font-size: 28px; font-weight: 400; letter-spacing: 1px; line-height: 1; margin-bottom: 10px; }
  .contact-list { list-style: none; }
  .contact-item {
    display: flex; align-items: center; gap: 10px;
    font-size: 16px; letter-spacing: 0.5px; line-height: 22px;
  }
  .contact-icon { width: 13px; height: 13px; flex: none; }
  .back-brand {
    position: absolute; right: 34px; bottom: 74px;
    font-size: 52px; line-height: 1;
  }
  .address {
    position: absolute; right: 34px; bottom: 24px;
    text-align: right; font-size: 16px; font-style: normal;
    letter-spacing: 0.5px; line-height: 1.3;
  }
</style>
</head>
<body>
<main class="canvas">
  <section class="card card--back" aria-label="Card back">
    <h2 class="holder-name">Marco Vell</h2>
    <ul class="contact-list">
      <li class="contact-item">
        <svg class="contact-icon" viewBox="0 0 16 16" aria-hidden="true"><path fill="#2b2b2b" d="M3 1h3l1.5 4-2 1.5a9 9 0 0 0 4 4L11 8.5 15 10v3a2 2 0 0 1-2 2A12 12 0 0 1 1 3a2 2 0 0 1 2-2z"/></svg>
        555 010 274
      </li>
      <li class="contact-item">
        <svg class="contact-icon" viewBox="0 0 16 16" aria-hidden="true"><rect x="1" y="3" width="14" height="10" fill="#2b2b2b"/><path d="M1 3l7 6 7-6" fill="none" stroke="#9a9a9a" stroke-width="1.2"/></svg>
        info@lucernaria-holding.com
      </li>
      <li class="contact-item">
        <svg class="contact-icon" viewBox="0 0 16 16" aria-hidden="true"><circle cx="8" cy="8" r="6.5" fill="none" stroke="#2b2b2b" stroke-width="1.5"/><path d="M1.5 8h13M8 1.5c-3 3.5-3 9.5 0 13M8 1.5c3 3.5 3 9.5 0 13" fill="none" stroke="#2b2b2b" stroke-width="1.2"/></svg>
        http://lucernaria-holding.com
      </li>
    </ul>
    <p class="back-brand">Lucernaria</p>
    <address class="address">Address line one<br>Address line two</address>
  </section>

  <section class="card card--front" aria-label="Card front">
    <h1 class="brand-name">Lucernaria</h1>
  </section>
</main>
</body>
</html>
```